Essential oil label for bottles

Looking to modify our current logo and label design. It looks too simple. I will attach images of our competitors to use as examples. Our company name is Velnora. We have 2 different bottles. Clear and amber color. Going forward, we will be using only the amber bottle. The other 2 images are the biggest sellers brands. We want to make some adjustments to ours.

Target Market(s)

Brindex sales

Industry/Entity Type

Essential oil, perfume

Colors

Designer to choose only greyscale colors for use in the design.

Requirements
Nice to have
• A slight change to fonts and logo design. Maybe change the font and design of the word "Velnora" in our logo. Maybe add something to the label to make it stand out more but still keeping it clean and modern
Should not have
• No colors, besides, black, grays, whites, and off white.

```html
<!DOCTYPE html>
<html lang="en">
<head>
<meta charset="UTF-8">
<title>Velnora – White Tea Fragrance Oil Label</title>
<link href="https://fonts.googleapis.com/css2?family=Questrial&display=swap" rel="stylesheet">
<style>
  :root {
    --backdrop: #f4f4f6;
    --label-black: #1a1715;
    --label-sheen: #2a2724;
    --ink-white: #f2f2f2;
  }
  html, body {
    margin: 0;
    padding: 0;
    width: 1200px;
    height: 1097px;
    overflow: hidden;
    background: var(--backdrop);
  }
  .canvas {
    position: relative;
    width: 1200px;
    height: 1097px;
    display: flex;
    align-items: center;
    justify-content: center;
  }
  .label {
    position: relative;
    width: 600px;
    height: 520px;
    background: linear-gradient(90deg, var(--label-black) 0%, var(--label-sheen) 30%, var(--label-black) 55%, #120f0d 100%);
    color: var(--ink-white);
    font-family: "Questrial", sans-serif;
    box-sizing: border-box;
  }
  .brand {
    position: absolute;
    left: 74px;
    top: 92px;
    display: flex;
    align-items: center;
    gap: 18px;
  }
  .brand-dot {
    width: 26px;
    height: 26px;
    border: 2px solid var(--ink-white);
    border-radius: 50%;
    box-sizing: border-box;
  }
  .brand-name {
    font-size: 24px;
    letter-spacing: 0.62em;
    text-transform: uppercase;
  }
  .product {
    position: absolute;
    left: 96px;
    top: 292px;
    width: 340px;
  }
  .product-name {
    margin: 0;
    font-size: 38px;
    font-weight: 400;
    letter-spacing: 0.01em;
    line-height: 1;
    text-transform: uppercase;
  }
  .product-type {
    margin: 6px 0 0;
    font-size: 15px;
    letter-spacing: 0.02em;
    text-transform: uppercase;
  }
  .product-rule {
    height: 0;
    border: 0;
    border-top: 2px solid var(--ink-white);
    margin: 6px 0 8px;
    width: 340px;
  }
  .product-notes {
    margin: 0;
    font-size: 15px;
    letter-spacing: 0.02em;
    text-transform: uppercase;
    white-space: nowrap;
  }
  .volume {
    position: absolute;
    left: 96px;
    bottom: 64px;
    font-size: 15px;
    letter-spacing: 0.02em;
  }
</style>
</head>
<body>
  <main class="canvas">
    <section class="label">
      <div class="brand">
        <span class="brand-dot" aria-hidden="true"></span>
        <span class="brand-name">Velnora</span>
      </div>
      <div class="product">
        <h1 class="product-name">White Tea</h1>
        <p class="product-type">Fragrance Oil</p>
        <hr class="product-rule">
        <p class="product-notes">White Tea &nbsp;|&nbsp; Orange &nbsp;|&nbsp; Palo Santo</p>
      </div>
      <div class="volume">200ML</div>
    </section>
  </main>
</body>
</html>
```